Marta Belle Designs & Events business card

I need an elegant informative but not busy business card using my logo. We are a florist with high end customers. I am adding a PDF file and a PNG file for those who requested it
Updates

Target Market(s)

Brides, grooms, men purchasing flowers
Ages 20-65

Industry/Entity Type

Florist

Requirements
Must have
• Business info:
Marta Belle Design & Events
www.martabelleevents-sample.com.
555-418-2763

555-418-2763
Nice to have
• Est 1954
may want Pinterest logo, twitter and linkedin and facbook
Should not have
• Clip art or photos

```html
<!DOCTYPE html>
<html lang="en">
<head>
<meta charset="utf-8">
<title>Marta Belle Designs &amp; Events — Business Card</title>
<link rel="stylesheet" href="https://fonts.googleapis.com/css2?family=Cormorant+SC:wght@500&family=Barlow:wght@400&family=Arimo:wght@400&display=swap">
<style>
  :root {
    --backdrop: #e8e5e1;
    --card: #ffffff;
    --navy: #1e2240;
    --ink: #2e3163;
    --pink: #f08cc8;
    --pink-soft: #f6b8dc;
    --shadow: rgba(0, 0, 0, 0.18);
  }
  * { margin: 0; padding: 0; box-sizing: border-box; }
  html, body {
    width: 1200px;
    height: 750px;
    overflow: hidden;
    background: var(--backdrop);
  }
  .canvas {
    position: relative;
    width: 1200px;
    height: 750px;
  }
  .card {
    position: absolute;
    background: var(--card);
    box-shadow: 0 6px 18px var(--shadow);
  }

  /* Front of card (landscape) */
  .card-front {
    left: 70px;
    top: 190px;
    width: 570px;
    height: 370px;
  }
  .corner-dot {
    position: absolute;
    width: 16px;
    height: 16px;
    border: 2px solid var(--pink);
    border-radius: 50%;
  }
  .corner-dot.tl { left: 26px; top: 26px; }
  .corner-dot.tr { right: 26px; top: 26px; }
  .corner-dot.bl { left: 26px; bottom: 26px; }
  .corner-dot.br { right: 26px; bottom: 26px; }
  .front-lockup {
    position: absolute;
    inset: 0;
    display: flex;
    flex-direction: column;
    align-items: center;
    justify-content: center;
  }
  .brand-mark {
    width: 92px;
    height: 92px;
    border: 3px solid var(--pink);
    border-radius: 50%;
    margin-bottom: 26px;
  }
  .brand-name {
    font-family: "Cormorant SC", "Times New Roman", serif;
    font-weight: 500;
    color: var(--navy);
    letter-spacing: 0.14em;
    line-height: 1;
  }
  .card-front .brand-name { font-size: 46px; }
  .brand-tagline {
    font-family: "Barlow", "Helvetica Neue", sans-serif;
    font-weight: 400;
    color: var(--pink);
    text-transform: uppercase;
    letter-spacing: 0.24em;
    line-height: 1;
  }
  .card-front .brand-tagline { font-size: 15px; margin-top: 10px; }

  /* Back of card (portrait) */
  .card-back {
    left: 703px;
    top: 87px;
    width: 410px;
    height: 610px;
    display: flex;
    flex-direction: column;
    align-items: center;
  }
  .card-back .brand-mark {
    width: 126px;
    height: 126px;
    margin-top: 66px;
    margin-bottom: 0;
  }
  .established {
    display: flex;
    align-items: center;
    gap: 10px;
    margin-top: 34px;
    font-family: "Cormorant SC", "Times New Roman", serif;
    font-weight: 500;
    font-size: 21px;
    color: var(--ink);
    letter-spacing: 0.04em;
  }
  .established .rule {
    width: 18px;
    height: 2px;
    background: var(--ink);
  }
  .card-back .brand-name {
    font-size: 33px;
    margin-top: 68px;
  }
  .card-back .brand-tagline {
    font-size: 14px;
    margin-top: 8px;
  }
  .contact {
    margin-top: 76px;
    text-align: center;
    font-family: "Arimo", Arial, sans-serif;
    color: var(--ink);
  }
  .contact-web { font-size: 20px; line-height: 1.2; }
  .contact-phone { font-size: 24px; letter-spacing: 0.04em; line-height: 1.3; }
  .social-bar {
    position: absolute;
    left: 34px;
    right: 34px;
    bottom: 44px;
    height: 27px;
    border-radius: 14px;
    background: var(--ink);
    display: flex;
    align-items: center;
    justify-content: space-between;
    padding: 0 14px;
  }
  .bar-end {
    width: 16px;
    height: 16px;
    border: 2px solid var(--card);
    border-radius: 50%;
  }
  .social-links {
    display: flex;
    gap: 22px;
    list-style: none;
  }
  .social-links li {
    width: 18px;
    height: 18px;
    border-radius: 3px;
    background: var(--pink);
  }
</style>
</head>
<body>
<main class="canvas">

  <section class="card card-front" aria-label="Business card front">
    <span class="corner-dot tl"></span>
    <span class="corner-dot tr"></span>
    <span class="corner-dot bl"></span>
    <span class="corner-dot br"></span>
    <div class="front-lockup">
      <span class="brand-mark"></span>
      <h1 class="brand-name">Marta Belle</h1>
      <p class="brand-tagline">Designs &amp; Events</p>
    </div>
  </section>

  <section class="card card-back" aria-label="Business card back">
    <span class="brand-mark"></span>
    <p class="established"><span class="rule"></span>Est 1954<span class="rule"></span></p>
    <h2 class="brand-name">Marta Belle</h2>
    <p class="brand-tagline">Designs &amp; Events</p>
    <div class="contact">
      <p class="contact-web">www.martabelleevents-sample.com</p>
      <p class="contact-phone">555-418-2763</p>
    </div>
    <div class="social-bar">
      <span class="bar-end"></span>
      <ul class="social-links" aria-label="Social media links">
        <li aria-label="Professional network"></li>
        <li aria-label="Pin board"></li>
        <li aria-label="Microblog"></li>
        <li aria-label="Social network"></li>
      </ul>
      <span class="bar-end"></span>
    </div>
  </section>

</main>
</body>
</html>
```